Magnetic Business card Design do a service provider

Hi,

The company aim is to provide all service needs under one roof. However, at the moment there is only Accounting, Electrical and IT branches. There will be more services coming onboard in the future.

I already have a logo designed (Company name is already part of the logo), I now need a magnetic business card designed.

The business card will contain the following:

- Company Logo
- Contact#
- E-mail
- enough space to add website URL (for future)
Updates

Project Deadline Extended Reason: HI All,The deadline has been extended due to not having enough time to review an overwhelming number of designs that has been submitted by lots of designers.I will be uploading a draft of designs that i have in mind.Thanks. Added Friday, January 22, 2016

Target Market(s)

Residential, Home-based Businesses, Small and Medium businesses

Industry/Entity Type

Business

Contact Information for Business Card

Contact#: 0491 738 552
E-mail: service@brightharborgroup.net.au

Font styles to use
Decorative
Script

Requirements
Must have
• Round edges
• Some form of logo incorporation as a background

```html
<!DOCTYPE html>
<html lang="en">
<head>
<meta charset="utf-8">
<title>Bright Harbor Group – Business Card</title>
<link href="https://fonts.googleapis.com/css2?family=Tinos&display=swap" rel="stylesheet">
<style>
  :root {
    --page-bg: #e9ebe8;
    --card-frost: #dde2dc;
    --card-frost-light: #eef1ec;
    --brand-blue: #0d3f7c;
    --brand-blue-dark: #0a2f60;
    --swoosh-grey: #8d918e;
    --name-navy: #123f78;
    --contact-text: #dfe6ee;
  }
  * { margin: 0; padding: 0; box-sizing: border-box; }
  html, body {
    width: 1200px;
    height: 952px;
    overflow: hidden;
    background: var(--page-bg);
  }
  .stage {
    position: relative;
    width: 1200px;
    height: 952px;
    display: flex;
    align-items: center;
    justify-content: center;
  }
  .business-card {
    position: relative;
    width: 1000px;
    height: 620px;
    border-radius: 36px;
    overflow: hidden;
    background: linear-gradient(160deg, var(--card-frost-light), var(--card-frost));
    box-shadow: 0 18px 40px rgba(0,0,0,0.18);
  }
  .card-art {
    position: absolute;
    inset: 0;
    width: 100%;
    height: 100%;
  }
  .brand-mark {
    position: absolute;
    left: 150px;
    top: 150px;
    display: flex;
    align-items: center;
    gap: 18px;
    white-space: nowrap;
  }
  .brand-dot {
    width: 44px;
    height: 44px;
    border-radius: 50%;
    background: var(--name-navy);
  }
  .brand-name {
    font-family: "Tinos", "Times New Roman", serif;
    font-size: 52px;
    line-height: 1;
    color: var(--name-navy);
  }
  .contact {
    position: absolute;
    font-family: "Tinos", "Times New Roman", serif;
    color: var(--contact-text);
    display: flex;
    align-items: center;
    gap: 18px;
    white-space: nowrap;
    line-height: 1;
  }
  .contact-phone { right: 44px; top: 384px; font-size: 38px; }
  .contact-web { left: 40px; top: 490px; font-size: 33px; }
  .contact-mail { left: 40px; top: 548px; font-size: 33px; }
  .contact-icon {
    width: 34px;
    height: 34px;
    flex: none;
  }
</style>
</head>
<body>
<main class="stage">
  <section class="business-card" aria-label="Bright Harbor Group business card">
    <svg class="card-art" viewBox="0 0 1000 620" aria-hidden="true">
      <path d="M0,440 C320,540 720,430 1000,40 L1000,620 L0,620 Z" fill="var(--brand-blue)"/>
      <path d="M0,560 C340,620 700,560 1000,300 L1000,620 L0,620 Z" fill="var(--brand-blue-dark)" opacity="0.35"/>
      <path d="M80,396 C380,486 740,380 960,70" fill="none" stroke="var(--swoosh-grey)" stroke-width="12" stroke-linecap="round"/>
    </svg>

    <div class="brand-mark">
      <span class="brand-dot"></span>
      <span class="brand-name">Bright Harbor Group</span>
    </div>

    <div class="contact contact-phone">
      <span>0491 738 552</span>
      <svg class="contact-icon" viewBox="0 0 34 34" aria-label="Phone">
        <rect x="1" y="1" width="32" height="32" rx="5" fill="none" stroke="var(--contact-text)" stroke-width="2"/>
        <path d="M11,9 l4,0 l1,5 l-3,2 c1,3 3,5 6,6 l2,-3 l5,1 l0,4 c-10,1 -16,-6 -15,-15 z" fill="var(--contact-text)"/>
      </svg>
    </div>

    <div class="contact contact-web">
      <svg class="contact-icon" viewBox="0 0 34 34" aria-label="Website">
        <rect x="1" y="1" width="32" height="32" rx="5" fill="none" stroke="var(--contact-text)" stroke-width="2"/>
        <circle cx="17" cy="17" r="10" fill="none" stroke="var(--contact-text)" stroke-width="2"/>
        <path d="M7,17 h20 M17,7 c-6,6 -6,14 0,20 M17,7 c6,6 6,14 0,20" fill="none" stroke="var(--contact-text)" stroke-width="1.6"/>
      </svg>
      <span>www.brightharborgroup.net.au</span>
    </div>

    <div class="contact contact-mail">
      <svg class="contact-icon" viewBox="0 0 34 34" aria-label="Email">
        <rect x="1" y="1" width="32" height="32" rx="5" fill="none" stroke="var(--contact-text)" stroke-width="2"/>
        <rect x="7" y="10" width="20" height="14" fill="none" stroke="var(--contact-text)" stroke-width="2"/>
        <path d="M7,10 l10,8 l10,-8" fill="none" stroke="var(--contact-text)" stroke-width="2"/>
      </svg>
      <span>service@brightharborgroup.net.au</span>
    </div>
  </section>
</main>
</body>
</html>
```